Copper Heron Motor Services needs a logo design

I'm after a logo design for a new Female owned automotive repair workshop in the Queanbeyan/Canberra Australia Area.
We offer repairs on all passenger cars, 4wds and light trucks emphasising a strong honest work ethic and a genuine interest in the customer and their vehicles needs. With business details on the front of the card and what we offer on the back.
I would like a design with a phoenix in multiple colours maybe hovering over a flaming wheel or a car with wheels flaming with the phoenix hovering up out of the flames
Target Market(s)
All Vehicle users
Industry/Entity Type
Automotive
Contact Information for Business Card
On the front
Copper Heron Motor
Maree Tolland Owner/ Mechanic 0413527806
email maree@copperheronmotor.com.au
Website www.copperheronmotorworks.com.au
On the back
All Cars, 4WDs, Light trucks, makes and models
Log book servicing
General vehicle servicing
Major vehicle servicing
brake and clutch servicing and repairs
Suspension repairs
cooling systems
All major and minor mechanical repairs
minor electrical rewiring and repairs
Colors
Designer to choose colors to be used in the design.
Look and feel

```html
<!DOCTYPE html>
<html lang="en">
<head>
<meta charset="utf-8">
<title>Copper Heron Motor – Business Cards</title>
<link rel="stylesheet" href="https://fonts.googleapis.com/css2?family=Open+Sans:wght@400;600;800&family=Oswald:wght@600&display=swap">
<style>
  :root {
    --bg: #ece9e4;
    --card-white: #ffffff;
    --card-black: #1c1a1b;
    --ink: #141414;
    --muted: #bdbdbd;
    --red-1: #e3060b;
    --red-2: #c9050a;
    --red-3: #a80509;
    --ribbon: #1e1e1e;
    --ribbon-fold: #000000;
    --text-light: #f2f2f2;
    --fire-dark: #1a1412;
    --fire-hot: #e8661a;
  }
  * { margin: 0; padding: 0; box-sizing: border-box; }
  html, body { width: 1200px; height: 1000px; overflow: hidden; }
  body { background: var(--bg); font-family: "Open Sans", sans-serif; position: relative; }

  .card {
    position: absolute; left: 250px; width: 700px; height: 400px;
    overflow: hidden; box-shadow: 0 10px 30px rgba(0,0,0,.18);
  }

  /* Back card */
  .card-back { top: 60px; background: var(--card-black); }
  .card-back__art { position: absolute; inset: 0; }
  .brand-mark {
    position: absolute; left: 60px; top: 52px;
    display: flex; align-items: center; gap: 14px;
    color: var(--card-white); font-weight: 800; font-size: 38px; line-height: 1;
  }
  .brand-dot { width: 22px; height: 22px; border-radius: 50%; background: var(--red-1); flex: none; }
  .brand-url {
    position: absolute; left: 62px; top: 104px;
    color: var(--muted); font-size: 12px; letter-spacing: 3px;
  }
  .service-list {
    position: absolute; left: 62px; top: 146px; list-style: none;
    color: var(--text-light); font-size: 13px; line-height: 17px;
  }
  .service-list li::before {
    content: ""; display: inline-block; width: 6px; height: 6px;
    background: var(--red-1); margin-right: 10px; vertical-align: middle;
  }

  /* Front card */
  .card-front { top: 540px; background: var(--card-white); }
  .card-front__art { position: absolute; inset: 0; }
  .holder {
    position: absolute; left: 30px; top: 300px;
  }
  .holder-name {
    font-family: "Oswald", sans-serif; font-weight: 600; font-size: 38px;
    color: var(--ink); letter-spacing: 1px; line-height: 1;
  }
  .holder-role {
    margin-top: 8px; font-size: 13px; font-weight: 600; letter-spacing: 2px; color: var(--red-2);
  }
  .contact-list { position: absolute; left: 0; top: 0; width: 700px; height: 400px; list-style: none; }
  .contact-item {
    position: absolute; width: 300px; height: 44px;
    background: var(--ribbon); color: var(--text-light);
    font-size: 12px; letter-spacing: .5px; white-space: nowrap;
    display: flex; align-items: center; justify-content: flex-end; gap: 12px;
    padding-right: 16px; transform: rotate(-4deg);
  }
  .contact-item::before {
    content: ""; position: absolute; left: -16px; top: 8px;
    width: 16px; height: 44px; background: var(--ribbon-fold);
    clip-path: polygon(0 0, 100% 0, 100% 100%, 40% 60%);
  }
  .contact-item--phone { top: 55px; left: 340px; }
  .contact-item--mail { top: 122px; left: 350px; }
  .contact-item--web { top: 189px; left: 360px; }
  .contact-item--area { top: 256px; left: 370px; }
  .contact-icon { width: 14px; height: 14px; flex: none; }
</style>
</head>
<body>

<section class="card card-back">
  <svg class="card-back__art" viewBox="0 0 700 400" width="700" height="400">
    <defs>
      <linearGradient id="backIllustration" x1="0" y1="1" x2="1" y2="0">
        <stop offset="0" stop-color="#f4f0ea"/>
        <stop offset=".45" stop-color="#f08a4b"/>
        <stop offset=".7" stop-color="#e0443a"/>
        <stop offset="1" stop-color="#4aa3c8"/>
      </linearGradient>
    </defs>
    <line x1="0" y1="366" x2="470" y2="366" stroke="var(--red-2)" stroke-width="2"/>
    <line x1="0" y1="378" x2="458" y2="378" stroke="var(--red-3)" stroke-width="2"/>
    <line x1="478" y1="372" x2="700" y2="178" stroke="var(--red-1)" stroke-width="3"/>
    <polygon points="470,400 700,196 700,400" fill="url(#backIllustration)"
             role="img" aria-label="Multicoloured phoenix rising out of a flaming wheel"/>
  </svg>
  <div class="brand-mark"><span class="brand-dot"></span>COPPER HERON MOTOR</div>
  <div class="brand-url">www.copperheronmotorworks.com.au</div>
  <ul class="service-list">
    <li>All Cars, 4WDs, Light trucks, makes and models</li>
    <li>Log book servicing</li>
    <li>General vehicle servicing</li>
    <li>Major vehicle servicing</li>
    <li>Brake and clutch servicing and repairs</li>
    <li>Suspension repairs</li>
    <li>Cooling systems</li>
    <li>All major and minor mechanical repairs</li>
    <li>Minor electrical rewiring and repairs</li>
  </ul>
</section>

<section class="card card-front">
  <svg class="card-front__art" viewBox="0 0 700 400" width="700" height="400">
    <defs>
      <radialGradient id="flamingWheel" cx=".45" cy=".45" r=".7">
        <stop offset="0" stop-color="#c9c9c9"/>
        <stop offset=".3" stop-color="var(--fire-hot)"/>
        <stop offset=".65" stop-color="#5a2a16"/>
        <stop offset="1" stop-color="var(--fire-dark)"/>
      </radialGradient>
    </defs>
    <polygon points="410,0 640,0 640,400 440,400" fill="var(--red-1)"/>
    <polygon points="480,0 560,0 580,400 500,400" fill="var(--red-2)"/>
    <polygon points="560,0 640,0 640,400 580,400" fill="var(--red-3)"/>
    <path d="M0 0 H245 Q215 250 0 290 Z" fill="url(#flamingWheel)"
          role="img" aria-label="Phoenix hovering over a car wheel engulfed in flames"/>
    <path d="M245 0 Q215 250 0 290" fill="none" stroke="var(--red-1)" stroke-width="5"/>
  </svg>

  <div class="holder">
    <h1 class="holder-name">MAREE TOLLAND</h1>
    <p class="holder-role">OWNER / MECHANIC</p>
  </div>

  <ul class="contact-list">
    <li class="contact-item contact-item--phone">0413527806
      <svg class="contact-icon" viewBox="0 0 16 16"><path d="M3 1h3l1.5 4-2 1.3a9 9 0 0 0 4.2 4.2L11 8.5l4 1.5v3c0 1-1 2-2 2A12 12 0 0 1 1 3c0-1 1-2 2-2z" fill="currentColor"/></svg>
    </li>
    <li class="contact-item contact-item--mail">maree@copperheronmotor.com.au
      <svg class="contact-icon" viewBox="0 0 16 16"><rect x="1" y="3" width="14" height="10" fill="none" stroke="currentColor" stroke-width="1.6"/><path d="M1 3l7 6 7-6" fill="none" stroke="currentColor" stroke-width="1.6"/></svg>
    </li>
    <li class="contact-item contact-item--web">www.copperheronmotorworks.com.au
      <svg class="contact-icon" viewBox="0 0 16 16"><circle cx="8" cy="8" r="6.5" fill="none" stroke="currentColor" stroke-width="1.5"/><ellipse cx="8" cy="8" rx="3" ry="6.5" fill="none" stroke="currentColor" stroke-width="1.2"/><line x1="1.5" y1="8" x2="14.5" y2="8" stroke="currentColor" stroke-width="1.2"/></svg>
    </li>
    <li class="contact-item contact-item--area">Queanbeyan / Canberra
      <svg class="contact-icon" viewBox="0 0 16 16"><path d="M8 1a5 5 0 0 0-5 5c0 4 5 9 5 9s5-5 5-9a5 5 0 0 0-5-5z" fill="currentColor"/><circle cx="8" cy="6" r="1.8" fill="var(--ribbon)"/></svg>
    </li>
  </ul>
</section>

</body>
</html>
```